Stationery Design For Specialist London law firm

We have merged two firms of London lawyers to create a new firm with a new name.

The new firms name is KR Holloway. We would like to include the description Solicitors and Advocates in the design.

We need a new design for our headed paper, business cards compliment slips etc.

The image we wish to project is fresh but not gimmicky - reliable and strong but not stuffy.

We have no strong views on font or colour this really is pretty much a blank page.

Our preference is for the name to be at the top of the page

Target Market(s)

Our clients who are individuals rather than corporate and other lawyers

Industry/Entity Type

Law Firm

Requirements
Should not have
• Legal images eg scales of justice etc

Obviously nothing childish or gimmicky

```html
<!DOCTYPE html>
<html lang="en">
<head>
<meta charset="utf-8">
<title>KR Holloway – Headed Paper and Business Card</title>
<link rel="stylesheet" href="https://fonts.googleapis.com/css2?family=Barlow:wght@400;600&family=Tinos&display=swap">
<style>
  :root {
    --navy: #1d2b4c;
    --rule-blue: #2a4f9c;
    --address-blue: #3a64a8;
    --orange: #f0a31c;
    --grey: #555b66;
    --ink: #1a1a1a;
    --paper: #ffffff;
  }
  * { margin: 0; padding: 0; box-sizing: border-box; }
  html, body { width: 1200px; height: 900px; overflow: hidden; background: var(--paper); }
  .letterhead { position: relative; width: 1200px; height: 900px; overflow: hidden; background: var(--paper); }

  /* header */
  .header-rules { position: absolute; left: 0; top: 0; }
  .brand { position: absolute; left: 722px; top: 42px; font-family: "Barlow", sans-serif; }
  .brand-name { font-weight: 600; font-size: 60px; line-height: 1; color: var(--navy); letter-spacing: 0.5px; }
  .brand-descriptor { margin-top: 10px; font-weight: 400; font-size: 22px; color: var(--orange); text-transform: uppercase; letter-spacing: 1.5px; }
  .firm-contact { position: absolute; left: 730px; top: 188px; font-family: "Barlow", sans-serif; font-size: 24px; line-height: 32px; color: var(--address-blue); }
  .firm-contact .phone { color: var(--rule-blue); font-weight: 600; }

  /* letter */
  .letter { font-family: "Tinos", serif; font-size: 25px; color: var(--ink); }
  .letter-date { position: absolute; left: 115px; top: 312px; }
  .letter-ref { position: absolute; left: 115px; top: 398px; }
  .recipient { position: absolute; left: 115px; top: 480px; line-height: 42px; }
  .salutation { position: absolute; left: 115px; top: 742px; }
  .letter-body { position: absolute; left: 115px; top: 790px; width: 1050px; line-height: 40px; }

  /* business card */
  .business-card { position: absolute; left: 351px; top: 495px; width: 522px; height: 337px; background: var(--paper); border: 1.5px solid var(--navy); font-family: "Barlow", sans-serif; }
  .card-rules { position: absolute; left: 0; top: 0; }
  .card-brand { position: absolute; left: 250px; top: 30px; }
  .card-brand .brand-name { font-weight: 600; font-size: 34px; line-height: 1; color: var(--navy); }
  .card-brand .brand-descriptor { margin-top: 7px; font-size: 13px; color: var(--orange); text-transform: uppercase; letter-spacing: 1px; }
  .card-person { position: absolute; left: 250px; top: 160px; font-size: 18px; line-height: 24px; color: var(--grey); }
  .card-person .person-name { color: var(--orange); font-weight: 600; font-size: 19px; }
  .card-contact { position: absolute; left: 22px; top: 160px; font-size: 18px; line-height: 24px; color: var(--grey); }
</style>
</head>
<body>
<main class="letterhead">

  <svg class="header-rules" width="1200" height="180" viewBox="0 0 1200 180" aria-hidden="true">
    <line x1="647" y1="0" x2="647" y2="173" stroke="var(--rule-blue)" stroke-width="2"/>
    <line x1="646" y1="173" x2="1200" y2="173" stroke="var(--rule-blue)" stroke-width="2"/>
  </svg>

  <div class="brand">
    <div class="brand-name">KR Holloway</div>
    <div class="brand-descriptor">Solicitors &amp; Advocates</div>
  </div>

  <address class="firm-contact" style="font-style:normal">
    42 Marlow Crescent<br>
    London E9 4QT<br>
    <span class="phone">T 0207 555 0148</span><br>
    M 0770 900 1234<br>
    E info@krholloway.co.uk<br>
    W www.krholloway.co.uk
  </address>

  <section class="letter">
    <p class="letter-date">24 November 2012</p>
    <p class="letter-ref">Your Ref: House move</p>
    <address class="recipient" style="font-style:normal">
      A M Crosby<br>
      Fernleigh House<br>
      Pelham Road<br>
      Northwich<br>
      Cheshire CW8 2LD
    </address>
    <p class="salutation">Dear Sir, madam</p>
    <p class="letter-body">Veritatis et quasi architecto beatae vitae dicta sunt explicabo. Nemo enim ipsam volupta tem quia voluptas sit aspernatur aut odit aut fugit, sed quia consequuntur magni dolores eos qui ratione voluptatem.</p>
  </section>

  <aside class="business-card">
    <svg class="card-rules" width="522" height="337" viewBox="0 0 522 337" aria-hidden="true">
      <line x1="209" y1="0" x2="209" y2="138" stroke="var(--rule-blue)" stroke-width="1.5"/>
      <line x1="208" y1="138" x2="522" y2="138" stroke="var(--rule-blue)" stroke-width="1.5"/>
    </svg>
    <div class="card-brand">
      <div class="brand-name">KR Holloway</div>
      <div class="brand-descriptor">Solicitors &amp; Advocates</div>
    </div>
    <div class="card-person">
      <div class="person-name">Martin Ashby</div>
      <div>partner</div>
      <div>M: 0779 210 4456</div>
    </div>
    <div class="card-contact">
      42 Marlow Crescent<br>
      London E9 4QT<br>
      T: 0207 555 0148<br>
      M: 0770 900 1234<br>
      E: info@krholloway.co.uk<br>
      W: www.krholloway.co.uk
    </div>
  </aside>

</main>
</body>
</html>
```